Creating a Label for the Wine "Fold the Sails"

As the name suggest, this wine is the one people must to take home. Fold the sails is the perfect wine to drink at home with you family and friends. Customers should be able to associate this label with happy moments spent with their loved ones. The dimensions can be between 9cm x 11,5 and 12cm x 8 cm.

```html
<!DOCTYPE html>
<html lang="en">
<head>
<meta charset="utf-8">
<title>Fold the Sails – Malbec 2014 label</title>
<link rel="stylesheet" href="https://fonts.googleapis.com/css2?family=Open+Sans:wght@700&family=Cormorant+Garamond:wght@500&display=swap">
<style>
  :root {
    --backdrop: #141414;
    --backdrop-light: #2c2c2c;
    --label: #2b2c2e;
    --label-edge: #232426;
    --ink: #f4f4f2;
    --accent: #8aa21c;
  }
  * { margin: 0; padding: 0; box-sizing: border-box; }
  html, body {
    width: 1200px;
    height: 3025px;
    overflow: hidden;
  }
  body {
    background: radial-gradient(ellipse at 50% 30%, var(--backdrop-light) 0%, var(--backdrop) 70%);
    position: relative;
  }
  .wine-label {
    position: absolute;
    left: 100px;
    top: 873px;
    width: 1000px;
    height: 1278px;
    background: linear-gradient(180deg, var(--label) 0%, var(--label-edge) 100%);
  }
  .aroma-ornament {
    position: absolute;
    left: 120px;
    top: 150px;
    width: 70px;
    height: 115px;
    border-radius: 35px;
    background: var(--accent);
    opacity: 0.85;
  }
  .wine-name {
    position: absolute;
    left: 120px;
    top: 300px;
    width: 760px;
    display: flex;
    align-items: flex-end;
    gap: 40px;
  }
  .name-mark {
    flex: 0 0 auto;
    width: 150px;
    height: 150px;
    background: var(--accent);
    margin-bottom: 38px;
  }
  .name-words {
    font-family: "Open Sans", sans-serif;
    font-weight: 700;
    font-size: 168px;
    line-height: 0.86;
    letter-spacing: -4px;
    color: var(--ink);
    text-align: right;
    flex: 1;
  }
  .name-words span { display: block; }
  .wine-details {
    position: absolute;
    left: 0;
    right: 0;
    top: 950px;
    text-align: center;
    font-family: "Cormorant Garamond", serif;
    font-weight: 500;
  }
  .grape {
    font-size: 46px;
    letter-spacing: 6px;
    color: var(--ink);
  }
  .vintage {
    font-size: 46px;
    letter-spacing: 10px;
    color: var(--accent);
    margin-top: 4px;
  }
</style>
</head>
<body>
  <section class="wine-label">
    <div class="aroma-ornament" role="img" aria-label="Small green curling aroma swirl ornament"></div>
    <h1 class="wine-name">
      <span class="name-mark" aria-hidden="true"></span>
      <span class="name-words">
        <span>fold</span>
        <span>the</span>
        <span>sails</span>
      </span>
    </h1>
    <div class="wine-details">
      <p class="grape">MALBEC</p>
      <p class="vintage">2014</p>
    </div>
  </section>
</body>
</html>
```